Safety Consultancy focusing on developing exceptional Safety Leaders

I need a full but simple, modern, catchy website to drive business - my focus is on helping organizations to understand the impact that leaders have on safety performance and how they build the processes to make that happen. I already have great branding (logos) built through PixelGuild and can provide all narrative to build out the pages

Target Market(s)

Focused internationally. Typical client has a fairly robust and mature safety culture yet lacks the focused effort to develop all levels of leadership in terms of managing safety. Exercising these competencies results in continued development of an organizations safety culture as well as improved safety performance

Industry/Entity Type

all

Coding

Coded - Design and coding required

Number of Pages Required

4 page

Font styles to use
Other font styles liked:
• to match my branding

Colors
0054AA
0677BA
7BADD7
CADEEF
E8F1F8

Requirements
Must have
• Must utilize my current branding, logo, etc. I want to have a page outlining clearly my vision - which I will add to my uploads as we move forward. I need to have a page listing my extensive and unique experience as well as successes
Nice to have
• Want to leave it up to designers - but needs to be simple and easily navigable - hope to have a resource page that I can update myself with safety resource info, reports, etc.

```html
<!DOCTYPE html>
<html lang="en">
<head>
<meta charset="utf-8">
<title>Castmoor Safety Partners</title>
<link href="https://fonts.googleapis.com/css2?family=Poppins:ital,wght@0,400;0,500;0,600;0,700;0,800;1,500&display=swap" rel="stylesheet">
<style>
:root{
  --navy:#2e3494;
  --navy-dark:#2b3175;
  --navy-band:#323a86;
  --ink:#222433;
  --text:#3a3a46;
  --grey-bg:#f0f0f0;
  --card-grey:rgba(214,214,218,.85);
  --lilac:#c9cbe2;
  --white:#fff;
  --dot:#c4c6d6;
}
*{margin:0;padding:0;box-sizing:border-box}
html,body{width:1200px;height:3988px;overflow:hidden}
body{position:relative;font-family:"Poppins",sans-serif;color:var(--text);background:var(--white)}
.abs{position:absolute}
a{color:inherit;text-decoration:none}
.btn{position:absolute;display:flex;align-items:center;justify-content:center;background:var(--navy);color:var(--white);font-weight:700;font-size:18px;letter-spacing:.3px;width:192px;height:54px}
.h2{position:absolute;font-size:56px;line-height:60px;color:var(--ink);font-weight:400}
.h2 b{color:var(--navy);font-weight:800}
.para{position:absolute;font-size:16px;line-height:30.5px;color:var(--text)}
.dots{position:absolute;background-image:radial-gradient(var(--dot) 2px,transparent 2.5px);background-size:22px 22px}

/* header */
.topbar{left:642px;top:0;width:558px;height:54px;background:#f3f3f3;display:flex;align-items:center;gap:14px;padding-left:46px;font-size:16px;color:var(--ink)}
.topbar .ic{width:36px;height:36px;border-radius:50%;background:var(--navy);display:flex;align-items:center;justify-content:center}
.topbar .gap{width:16px}
.brand{left:74px;top:36px;display:flex;align-items:center;gap:14px}
.brand .mark{width:26px;height:26px;background:var(--navy)}
.brand span{font-size:50px;font-weight:700;color:var(--navy);letter-spacing:-.5px}
.nav{left:590px;top:90px;display:flex;gap:31px;font-size:15px;font-weight:500;color:var(--ink)}
.nav .on{color:var(--navy)}

/* hero */
.hero{left:0;top:144px;width:1200px;height:666px}
.hero h1{position:absolute;left:0;width:1200px;top:222px;text-align:center;color:var(--white);font-size:78px;line-height:70px;font-weight:800}
.hero p{position:absolute;left:0;width:1200px;top:370px;text-align:center;color:var(--white);font-size:31px;line-height:45px;font-weight:700}
.hero .btn{left:503px;top:475px;width:192px;height:54px}
.hero .dot{position:absolute;top:598px;width:14px;height:14px;border-radius:50%;background:var(--white)}

/* services */
.svc{position:absolute;width:297px;height:206px;border-radius:38px;display:flex;flex-direction:column;align-items:center;justify-content:center;gap:14px;text-align:center;font-weight:700;font-size:18px;line-height:25px;color:var(--navy)}
.svc.main{background:var(--navy);color:var(--white);z-index:3}
.svc.soft{background:var(--card-grey)}

/* welcome */
.welcome{left:0;top:1469px;width:1200px;height:579px;background:var(--grey-bg);overflow:hidden}

/* blog */
.blogband{left:0;top:2729px;width:1200px;height:400px;background:var(--navy-band)}
.post{position:absolute;top:2885px;width:328px;height:459px;background:var(--white);border:1px solid #dcdcdc}
.post.active{border-color:var(--navy)}
.post .img{height:271px}
.post .date{position:absolute;left:21px;top:300px;font-size:13px;font-weight:500;color:var(--navy)}
.post h3{position:absolute;left:21px;top:322px;width:290px;font-size:22px;line-height:31px;font-weight:600;color:var(--ink)}
.post .rule{position:absolute;left:0;right:0;top:397px;border-top:1px solid #e2e2e2}
.post .more{position:absolute;left:21px;top:418px;font-size:16px;color:var(--navy)}

/* footer */
.footer{left:0;top:3423px;width:1200px;height:565px;background:var(--navy-dark);color:var(--white)}
.fcontact{position:absolute;top:30px;display:flex;gap:14px}
.fcontact h4{font-size:18px;font-weight:600;letter-spacing:.3px}
.fcontact p{font-size:15px;line-height:23px;margin-top:6px;color:#e4e5f0}
.fcol{position:absolute;top:198px}
.fcol h5{font-size:18px;font-weight:700;margin-bottom:18px;letter-spacing:.3px}
.fcol li{list-style:none;font-size:15px;color:#e0e2ee}
.copy{position:absolute;left:0;width:1200px;top:514px;text-align:center;font-size:14px;color:#d8daea}
</style>
</head>
<body>

<!-- Header -->
<div class="abs topbar">
  <span class="ic"><svg width="16" height="16" viewBox="0 0 24 24" fill="#fff"><path d="M6.6 10.8a15 15 0 006.6 6.6l2.2-2.2c.3-.3.7-.4 1-.2 1.1.4 2.3.6 3.6.6.6 0 1 .4 1 1V20c0 .6-.4 1-1 1A17 17 0 013 4c0-.6.4-1 1-1h3.5c.6 0 1 .4 1 1 0 1.3.2 2.5.6 3.6.1.3 0 .7-.2 1z"/></svg></span>
  <span>1-555-014-2290</span>
  <span class="gap"></span>
  <span class="ic"><svg width="16" height="16" viewBox="0 0 24 24" fill="#fff"><path d="M2 5h20v14H2z" opacity="0"/><path d="M3 6h18v12H3zM3 6l9 7 9-7" fill="none" stroke="#fff" stroke-width="2"/></svg></span>
  <span>hello@castmoor.example</span>
</div>
<div class="abs brand"><span class="mark"></span><span>Castmoor</span></div>
<nav class="abs nav">
  <a class="on">HOME</a><a>ABOUT US</a><a>SERVICES</a><a>CLIENTS</a><a>BLOG</a><a>CONTACT US</a>
</nav>

<!-- Hero -->
<section class="abs hero">
  <svg class="abs" width="1200" height="666" style="left:0;top:0" role="img" aria-label="Photo of two safety engineers in hard hats talking at a construction site with cranes">
    <defs><linearGradient id="heroG" x1="0" y1="0" x2="1" y2="1"><stop offset="0" stop-color="#5f7c98"/><stop offset=".5" stop-color="#3d4f66"/><stop offset="1" stop-color="#8a9cad"/></linearGradient></defs>
    <path d="M0 0H1200V560L600 666 0 560Z" fill="url(#heroG)"/>
  </svg>
  <h1>Castmoor Safety<br>Partners</h1>
  <p>We are a Safety Consultancy focusing on developing<br>exceptional Safety Leaders.</p>
  <a class="btn">READ MORE</a>
  <span class="dot" style="left:561px;background:var(--navy)"></span>
  <span class="dot" style="left:584px"></span>
  <span class="dot" style="left:608px"></span>
  <span class="dot" style="left:631px"></span>
</section>

<!-- Services -->
<div class="dots" style="left:0;top:876px;width:70px;height:250px"></div>
<h2 class="h2" style="left:74px;top:953px"><b>Our<br>Services</b> Offer</h2>
<p class="para" style="left:74px;top:1086px;width:510px">Sed ut perspiciatis unde omnis iste natus error sit voluptatem accusantium doloremque laudantium, totam rem aperiam, eaque ipsa quae ab illo inventore veritatis et quasi architecto beatae vitae dicta sunt explicabo. Nemo enim ipsam voluptatem quia voluptas sit aspernatur aut odit aut fugit, sed quia consequuntur magni dolores eos qui ratione voluptatem sequi nesciunt.</p>
<a class="btn" style="left:74px;top:1322px">READ MORE</a>

<div class="dots" style="left:950px;top:1140px;width:250px;height:250px"></div>
<div class="svc main" style="left:568px;top:981px">
  <svg width="60" height="64" viewBox="0 0 60 64" fill="none" stroke="#fff" stroke-width="2.5"><path d="M30 3L54 12V30C54 46 43 56 30 61 17 56 6 46 6 30V12Z"/><circle cx="30" cy="31" r="14"/><path d="M26 22h8v5h5v8h-5v5h-8v-5h-5v-8h5z"/></svg>
  <span>IPSAM<br>VOLUPTATEM</span>
</div>
<div class="svc soft" style="left:828px;top:981px">
  <svg width="60" height="62" viewBox="0 0 60 62" fill="none" stroke="#2e3494" stroke-width="2.5"><circle cx="30" cy="18" r="12"/><circle cx="30" cy="18" r="4"/><circle cx="14" cy="40" r="6"/><circle cx="46" cy="40" r="6"/><path d="M4 58c0-8 5-12 10-12s10 4 10 12M36 58c0-8 5-12 10-12s10 4 10 12"/></svg>
  <span>IPSAM<br>VOLUPTATEM</span>
</div>
<div class="svc soft" style="left:698px;top:1152px;z-index:2">
  <svg width="64" height="64" viewBox="0 0 64 64" fill="none" stroke="#2e3494" stroke-width="2.5"><path d="M16 22a14 14 0 0128 0M12 22h36"/><path d="M20 24c0 8 5 14 10 14s10-6 10-14"/><path d="M8 62c0-12 10-20 22-20s22 8 22 20"/><path d="M46 40l10 4v8c0 6-4 9-10 11-6-2-10-5-10-11v-8z"/><path d="M42 52l3 3 6-6"/></svg>
  <span>IPSAM<br>VOLUPTATEM</span>
</div>

<!-- Welcome -->
<section class="abs welcome">
  <div class="abs" role="img" aria-label="Photo of two business professionals in a modern office" style="left:74px;top:94px;width:460px;height:391px;border-radius:80px 0 195px 195px;background:linear-gradient(135deg,#c8ccd4,#8d95a4 60%,#5d6675)"></div>
  <div class="abs" style="left:1079px;top:121px;width:124px;height:124px;border-radius:50%;background:var(--lilac)"></div>
  <h2 class="h2" style="left:616px;top:70px"><b>Welcome to</b><br>Castmoor Safety</h2>
  <p class="para" style="left:616px;top:206px;width:520px">Sed ut perspiciatis unde omnis iste natus error sit voluptatem accusantium doloremque laudantium, totam rem aperiam, eaque ipsa quae ab illo inventore veritatis et quasi architecto beatae vitae dicta sunt explicabo. Nemo enim ipsam voluptatem quia voluptas sit aspernatur aut odit aut fugit, sed quia consequuntur magni dolores eos qui ratione voluptatem sequi nesciunt.</p>
  <a class="btn" style="left:616px;top:441px">READ MORE</a>
</section>

<!-- CEO -->
<h2 class="h2" style="left:74px;top:2184px"><b>Message<br>From</b> CEO</h2>
<p class="abs" style="left:74px;top:2324px;font-size:27px;font-style:italic;font-weight:500;color:var(--ink)">Daniel K. Castmoor, CRSP</p>
<p class="para" style="left:74px;top:2372px;width:500px;font-size:16px;line-height:27px">“ Sed ut perspiciatis unde omnis iste natus error sit voluptatem accusantium doloremque laudantium, totam rem aperiam, eaque ipsa quae ab illo inventore veritatis et quasi architecto beatae vitae dicta sunt explicabo...”</p>
<a class="btn" style="left:74px;top:2519px">READ MORE</a>
<div class="dots" style="left:1030px;top:2086px;width:170px;height:250px"></div>
<div class="dots" style="left:536px;top:2460px;width:240px;height:240px"></div>
<svg class="abs" style="left:573px;top:2127px" width="552" height="512" role="img" aria-label="Portrait photo of the company founder in a blue suit in front of city towers">
  <defs><linearGradient id="ceoG" x1="0" y1="0" x2="1" y2="1"><stop offset="0" stop-color="#6d89b8"/><stop offset=".55" stop-color="#2f4f8f"/><stop offset="1" stop-color="#1e2f62"/></linearGradient></defs>
  <path d="M0 512L88 0H552V512Z" fill="#fff"/>
  <path d="M0 512L88 0H98L12 512Z" fill="var(--navy)"/>
  <path d="M22 512L108 0H552V512Z" fill="url(#ceoG)"/>
</svg>

<!-- Blog -->
<div class="abs blogband"></div>
<h2 class="h2" style="left:0;width:1200px;top:2790px;text-align:center;color:var(--white)"><b style="color:var(--white)">Latest</b> Blog</h2>
<article class="post" style="left:74px">
  <div class="img" role="img" aria-label="Photo of two colleagues in a warehouse, one in a high-visibility vest" style="background:linear-gradient(135deg,#9aa5ad,#5b6672 60%,#c98a54)"></div>
  <span class="date">AUG 04, 2024</span>
  <h3>Sed ut perspiciatis unde omnis iste natus</h3>
  <div class="rule"></div><a class="more">READ MORE</a>
</article>
<article class="post active" style="left:437px">
  <div class="img" role="img" aria-label="Photo of a single blue umbrella among many black umbrellas" style="background:radial-gradient(circle at 50% 50%,#2f7fd0 0,#2f7fd0 20%,#2b2f36 45%,#15181d 100%)"></div>
  <span class="date">AUG 04, 2024</span>
  <h3>Sed ut perspiciatis unde omnis iste natus</h3>
  <div class="rule"></div><a class="more">READ MORE</a>
</article>
<article class="post" style="left:797px">
  <div class="img" role="img" aria-label="Photo of construction workers in hard hats smiling on site" style="background:linear-gradient(135deg,#c9ccce,#8e8f7e 50%,#5c6450)"></div>
  <span class="date">AUG 04, 2024</span>
  <h3>Sed ut perspiciatis unde omnis iste natus</h3>
  <div class="rule"></div><a class="more">READ MORE</a>
</article>

<!-- Footer -->
<footer class="abs footer">
  <div class="abs" style="left:483px;top:0;height:145px;border-left:1px solid rgba(255,255,255,.25)"></div>
  <div class="abs" style="left:833px;top:0;height:145px;border-left:1px solid rgba(255,255,255,.25)"></div>
  <div class="abs" style="left:0;right:0;top:145px;border-top:1px solid rgba(255,255,255,.25)"></div>
  <div class="fcontact" style="left:74px">
    <svg width="34" height="26" viewBox="0 0 34 26" fill="#fff"><path d="M0 3l10-3 12 3 12-3v23l-12 3-12-3-10 3z" opacity=".9"/></svg>
    <div><h4>LOCATION</h4><p>1420 Harbor Lane, Westfield, British<br>Columbia, Canada. V0X 1A0</p></div>
  </div>
  <div class="fcontact" style="left:550px">
    <svg width="22" height="26" viewBox="0 0 24 24" fill="#fff"><path d="M6.6 10.8a15 15 0 006.6 6.6l2.2-2.2c.3-.3.7-.4 1-.2 1.1.4 2.3.6 3.6.6.6 0 1 .4 1 1V20c0 .6-.4 1-1 1A17 17 0 013 4c0-.6.4-1 1-1h3.5c.6 0 1 .4 1 1 0 1.3.2 2.5.6 3.6.1.3 0 .7-.2 1z"/></svg>
    <div><h4>CALL US</h4><p style="font-size:20px">555-014-2290</p></div>
  </div>
  <div class="fcontact" style="left:856px">
    <svg width="32" height="24" viewBox="0 0 32 24" fill="none" stroke="#fff" stroke-width="2.5"><path d="M2 2h28v20H2zM2 2l14 11L30 2"/></svg>
    <div><h4>EMAIL US</h4><p style="font-size:14px">hello@castmoor.example</p></div>
  </div>

  <div class="fcol" style="left:73px"><h5>COMPANY</h5><ul style="line-height:37px"><li>Home</li><li>About Us</li><li>Services</li><li>Clients</li><li>Blog</li><li>Contact Us</li></ul></div>
  <div class="fcol" style="left:342px"><h5>SERVICES</h5><ul style="line-height:42px"><li>Nemo Enim Ipsam</li><li>Voluptatem</li><li>Quia Voluptas Sit</li><li>Aspernatur Untur</li><li>Magni Dolores</li></ul></div>
  <div class="fcol" style="left:616px"><h5>RESOURCES</h5><ul style="line-height:42px"><li>Nemo Enim Ipsam</li><li>Voluptatem</li><li>Quia Voluptas Sit</li><li>Aspernatur Untur</li><li>Magni Dolores</li></ul></div>
  <div class="fcol" style="left:883px;width:242px">
    <h5>NEWSLETTER</h5>
    <p style="font-size:15px;line-height:25px;color:#e0e2ee">Nemo enim ipsam voluptatem quia voluptas sit</p>
    <div style="margin-top:20px;height:53px;border:1px solid rgba(255,255,255,.6);display:flex;align-items:center;padding-left:16px;font-size:14px">Enter Email</div>
    <div style="margin-top:12px;height:53px;background:#d9d9d9;color:var(--ink);display:flex;align-items:center;justify-content:center;font-weight:700;font-size:17px">SUBSCRIBE</div>
  </div>
  <p class="copy">Copyright ©2024 CompanyName  All Rights Reserved. Privacy policy | Terms &amp; conditions</p>
</footer>

</body>
</html>
```